Website design for dressage horse training business

Looking to develop a new website design for a dressage horse training website. We want to change from a single landing page to one with multiple pages.
You are free to use your creativity to design the main landing page. This is the only page you need to design at this point. I would encourage looking at other Dressage Training websites to get a feel for what is typically on them. A few websites are listed below although I think the design of them could be better.
Notes:
- Menu to include: Home, Services, News Room, Blog, About Us, Contact,
- FAQ section on main page
- Logo to remain the same - the logo attached is not the correct color so change to match existing color.
- Change 'Sponsors' to 'Partnerships' on main page
Here is the link to the current site:
https://lindenridgestables.com/
Example sites
https://www.crestwoodsporthorsesco.com/
https://corinnalavelledressage.com/
Target Market(s)
Older women with disposable income
Number of Pages Required
1 page
Look and feel
Each slider illustrates characteristics of the customer's brand and the style your logo design should communicate.

```html
<!DOCTYPE html>
<html lang="en">
<head>
<meta charset="utf-8">
<title>Linden Ridge Stables — Dressage &amp; Sport Horse Training</title>
<link rel="stylesheet" href="https://fonts.googleapis.com/css2?family=Cinzel:wght@400;500&family=Open+Sans:ital,wght@0,400;0,600;1,400&display=swap">
<style>
:root{
  --tan:#c3a07c;
  --tan-dark:#a9855f;
  --ink:#222222;
  --text:#666666;
  --light:#f6f5f3;
  --faq-bg:#ededec;
  --footer:#1c1c1c;
  --white:#ffffff;
}
*{box-sizing:border-box;margin:0;padding:0}
html,body{width:1200px;height:4988px;overflow:hidden}
body{position:relative;font-family:"Open Sans",Arial,sans-serif;color:var(--text);background:var(--white)}
.section{position:absolute;left:0;width:1200px;overflow:hidden}
.abs{position:absolute}
.serif{font-family:"Cinzel",Georgia,serif;font-weight:400}
.pill{position:absolute;display:flex;align-items:center;justify-content:center;border-radius:30px;font-size:17px;letter-spacing:.5px}
.pill.tan{background:var(--tan);color:var(--white)}
.section-title{position:absolute;left:0;width:1200px;text-align:center;font-family:"Cinzel",Georgia,serif;font-size:46px;color:var(--ink);letter-spacing:1px}

/* header */
.site-header{top:0;height:100px;background:var(--white)}
.brand{position:absolute;left:110px;top:18px;color:var(--tan);font-family:"Cinzel",Georgia,serif;font-weight:400;line-height:1}
.brand .name{font-size:38px;letter-spacing:1px}
.brand .sub{font-size:14px;letter-spacing:14px;margin-top:6px;padding-left:40px}
.header-phone{position:absolute;right:110px;top:18px;font-size:17px;color:var(--ink);display:flex;align-items:center;gap:8px}
.main-nav{position:absolute;right:110px;top:58px;display:flex;gap:28px;font-size:15.5px;color:var(--ink);letter-spacing:.3px}
.main-nav .active{color:var(--tan)}

/* hero */
.hero{top:100px;height:576px;background:linear-gradient(180deg,#93a7b7 0%,#b6c3cd 45%,#8d9591 80%,#6f756f 100%)}
.hero-photo{position:absolute;left:0;top:0;width:1200px;height:576px}
.hero-ring{position:absolute;left:445px;top:-30px;width:560px;height:560px;border-radius:50%;background:rgba(255,255,255,.18)}
.hero-title{left:112px;top:130px;font-size:63px;color:var(--white);letter-spacing:1px}
.hero-sub{left:112px;top:222px;font-size:24px;line-height:36px;color:var(--white)}
.hero .pill{left:112px;top:328px;width:203px;height:60px;background:var(--white);color:var(--ink);font-size:19px}
.dots{position:absolute;display:flex;gap:6px}
.dot{width:13px;height:13px;border-radius:50%;border:2px solid var(--white)}
.dot.on{background:var(--white)}

/* welcome */
.welcome{top:676px;height:626px;background:var(--white)}
.welcome-photo{position:absolute;left:0;top:0;width:630px;height:560px;background:linear-gradient(135deg,#d9d9d9,#8d8d8d 55%,#3a3a3a)}
.welcome-kicker{left:670px;top:70px;font-size:30px;color:var(--ink)}
.welcome-title{left:670px;top:104px;font-size:50px;color:var(--ink)}
.welcome-copy{position:absolute;left:670px;top:190px;width:420px;font-size:14.5px;line-height:28.5px}
.welcome-copy p+p{margin-top:28px}
.welcome .pill{left:670px;top:508px;width:162px;height:54px}

/* services */
.services{top:1302px;height:920px;background:var(--light)}
.service-name{font-size:29px;font-weight:600;color:var(--ink);letter-spacing:.5px}
.service-copy{position:absolute;width:470px;font-size:15px;line-height:26.5px}
.video{position:absolute;width:463px;height:314px;box-shadow:0 3px 10px rgba(0,0,0,.25)}
.video .play{position:absolute;left:50%;top:50%;transform:translate(-50%,-50%)}
.services .pill{width:162px;height:54px}

/* testimonial */
.testimonial{top:2222px;height:584px;background:linear-gradient(100deg,#8a7d6c 0%,#b99b72 30%,#f2a544 52%,#9a5d24 70%,#3a2612 100%)}
.quote-halo{position:absolute;left:73px;top:23px;width:520px;height:520px;border-radius:50%;background:rgba(255,255,255,.25)}
.quote-card{position:absolute;left:105px;top:55px;width:456px;height:456px;border-radius:50%;background:var(--white);text-align:center}
.quote-mark{position:absolute;left:0;width:100%;top:40px;font-family:"Cinzel",Georgia,serif;font-size:110px;color:var(--tan);line-height:1}
.quote-text{position:absolute;left:55px;top:140px;width:346px;font-style:italic;font-size:15.5px;line-height:26px;color:var(--text)}
.quote-name{position:absolute;left:0;width:100%;top:300px;font-size:21px;color:var(--ink)}
.quote-role{position:absolute;left:0;width:100%;top:330px;font-size:17px;color:var(--ink)}
.dot.grey{border-color:#777}
.dot.grey.on{background:#777}

/* faq */
.faq{top:2806px;height:713px;background:var(--faq-bg)}
.faq-item{position:absolute;left:112px;width:976px;background:var(--white);border:1px solid #d5d5d5}
.faq-q{position:absolute;left:18px;top:14px;font-size:20px;color:var(--ink)}
.faq-a{position:absolute;left:18px;top:54px;width:760px;font-size:15px;line-height:26.5px;color:#888}
.toggle{position:absolute;right:-1px;top:-1px;width:62px;height:60px;background:var(--ink);display:flex;align-items:center;justify-content:center}
.toggle.open{background:var(--tan)}

/* partnerships */
.partners{top:3519px;height:565px;background:var(--white)}
.partner-card{position:absolute;top:167px;width:476px;height:314px;border:3px solid var(--ink);text-align:center}
.partner-card.alt{border-color:var(--tan)}
.partner-mark{position:absolute;left:0;width:100%;top:42px;display:flex;align-items:center;justify-content:center;gap:10px;font-family:"Cinzel",Georgia,serif;font-size:26px;color:var(--tan-dark)}
.partner-mark .badge{width:22px;height:22px;border-radius:50%;background:var(--tan-dark)}
.partner-copy{position:absolute;left:22px;width:426px;top:178px;font-size:15.5px;line-height:26px;color:var(--text)}
.partner-link{position:absolute;left:0;width:100%;top:262px;font-size:16px;color:var(--tan);letter-spacing:.5px}

/* contact */
.contact{top:4084px;height:519px;background:linear-gradient(110deg,#3a3a3a 0%,#6b6b6b 35%,#9a9a9a 60%,#4a4a4a 85%,#2e2e2e 100%)}
.contact-title{left:115px;top:80px;font-size:48px;color:var(--white)}
.field{position:absolute;background:var(--white);font-size:15.5px;color:#888;padding:12px 14px}
.contact .pill{left:112px;top:363px;width:127px;height:55px}

/* footer */
.site-footer{top:4603px;height:385px;background:var(--footer)}
.footer-brand{position:absolute;left:112px;top:88px;color:var(--tan);font-family:"Cinzel",Georgia,serif;line-height:1}
.footer-brand .name{font-size:66px;letter-spacing:1px}
.footer-brand .sub{font-size:22px;letter-spacing:24px;margin-top:12px;padding-left:70px}
.footer-col{position:absolute;top:52px;color:var(--white);font-size:15.5px}
.footer-col h4{font-family:"Cinzel",Georgia,serif;font-weight:400;font-size:17px;letter-spacing:.5px;margin-bottom:14px}
.footer-col li{list-style:none;line-height:28.5px;display:flex;align-items:center;gap:9px}
.footer-rule{position:absolute;left:112px;top:287px;width:976px;height:1px;background:#3a3a3a}
.copyright{position:absolute;left:112px;top:323px;color:var(--white);font-size:15.5px}
.socials{position:absolute;right:110px;top:305px;display:flex;gap:8px}
.socials span{width:44px;height:44px;border-radius:50%;border:2px solid var(--white)}
</style>
</head>
<body>

<header class="section site-header">
  <div class="brand"><div class="name">LINDEN RIDGE</div><div class="sub">STABLES</div></div>
  <div class="header-phone">
    <svg width="14" height="14" viewBox="0 0 24 24"><path fill="#c3a07c" d="M6.6 10.8a15 15 0 0 0 6.6 6.6l2.2-2.2c.3-.3.7-.4 1-.2 1.1.4 2.3.6 3.6.6.6 0 1 .4 1 1V20c0 .6-.4 1-1 1A17 17 0 0 1 3 4c0-.6.4-1 1-1h3.5c.6 0 1 .4 1 1 0 1.3.2 2.5.6 3.6.1.3 0 .7-.2 1z"/></svg>
    555-014-2290
  </div>
  <nav class="main-nav">
    <span class="active">HOME</span><span>SERVICES</span><span>NEWS ROOM</span><span>BLOG</span><span>ABOUT US</span><span>CONTACT</span>
  </nav>
</header>

<section class="section hero">
  <div class="hero-photo" role="img" aria-label="Rider in show attire on a grey dressage horse under a pale sky"></div>
  <div class="hero-ring"></div>
  <h1 class="abs serif hero-title">LINDEN RIDGE</h1>
  <p class="abs hero-sub">Central Iowa's Premier dressage<br>and sport horse training</p>
  <div class="pill">GET STARTED</div>
  <div class="dots" style="left:562px;top:506px"><span class="dot on"></span><span class="dot"></span><span class="dot"></span><span class="dot"></span></div>
</section>

<section class="section welcome">
  <div class="welcome-photo" role="img" aria-label="Dappled grey horse jumping with rider, cut out on white"></div>
  <div class="abs serif welcome-kicker">WELCOME TO</div>
  <h2 class="abs serif welcome-title">LINDEN RIDGE</h2>
  <div class="welcome-copy">
    <p>FEI rider and trainer, Clara Hensley began her riding career at a young age.</p>
    <p>She went up through the ranks of Pony Club and with an emphasis and focus in eventing. During college, Clara worked for a small breeder starting young horses. Clara loves starting young horses including starting and guiding them in a correct and quiet way to help them flourish. Her training focuses on gymnastic training incorporating ground work/lunging/long lining.</p>
  </div>
  <div class="pill tan">READ MORE</div>
</section>

<section class="section services">
  <h2 class="section-title" style="top:50px">SERVICES</h2>

  <h3 class="abs service-name" style="left:112px;top:158px">TRAINING</h3>
  <p class="service-copy" style="left:112px;top:215px">Linden Ridge offers both full and half time training options with Clara Hensley. There is much flexibility with both rides and/or lessons weekly in the training packages that can be customized to fit both the horse and the rider's needs. Generally, full training provides 3-4 "working days" of riding, and 1-2 "light" days consisting..</p>
  <div class="pill tan" style="left:112px;top:404px">READ MORE</div>
  <div class="video" style="left:625px;top:150px;background:linear-gradient(180deg,#3f5a34 0%,#7f8f6a 35%,#d8d2c6 60%,#cfc8bb 100%)" role="img" aria-label="Trainer lunging a grey horse with rider in an outdoor arena">
    <svg class="play" width="56" height="56" viewBox="0 0 56 56"><circle cx="28" cy="28" r="27" fill="rgba(0,0,0,.45)" stroke="#fff" stroke-width="2"/><path d="M22 17 L40 28 L22 39Z" fill="#fff"/></svg>
  </div>

  <div class="video" style="left:112px;top:518px;background:linear-gradient(180deg,#5a4630 0%,#a98a5e 40%,#6b4e2f 75%,#3b2a1a 100%)" role="img" aria-label="Rider on a chestnut horse in a sunlit indoor arena">
    <svg class="play" width="56" height="56" viewBox="0 0 56 56"><circle cx="28" cy="28" r="27" fill="rgba(0,0,0,.45)" stroke="#fff" stroke-width="2"/><path d="M22 17 L40 28 L22 39Z" fill="#fff"/></svg>
  </div>
  <h3 class="abs service-name" style="left:617px;top:526px">LESSONS</h3>
  <p class="service-copy" style="left:617px;top:583px">Lessons are available for all ages of riders. Clara thoroughly enjoys working with accomplished riders looking to succeed in the show ring, as well as riders just wanting to learn what dressage is about. Come join our incredible and encouraging team!</p>
  <div class="pill tan" style="left:617px;top:752px">READ MORE</div>
</section>

<section class="section testimonial" role="img" aria-label="Two riders on horseback silhouetted against a golden sunset">
  <div class="quote-halo"></div>
  <div class="quote-card">
    <div class="quote-mark">&ldquo;</div>
    <p class="quote-text">Nemo enim ipsam voluptatem quia volup tas sit aspernatur aut odit aut fugit, sed quia consequuntur magni dolores eos qui ratione voluptatem sequi nesciunt. Neque porro quisquam est, qui dolorem ipsum quia dolor sit amet, consectetur, adipisci.</p>
    <div class="quote-name">Henry,</div>
    <div class="quote-role">Finibus Bonoru</div>
    <div class="dots" style="left:202px;top:390px"><span class="dot grey on"></span><span class="dot grey"></span><span class="dot grey"></span></div>
  </div>
</section>

<section class="section faq">
  <h2 class="section-title" style="top:80px">FAQ</h2>
  <div class="faq-item" style="top:181px;height:152px">
    <div class="faq-q">Sed ut perspiciatis unde omnis iste natus error sit voluptatem accusantiu?</div>
    <p class="faq-a">Nemo enim ipsam voluptatem quia voluptas sit aspernatur aut odit aut fugit, sed quia conseq uu ntur magni dolores eos qui ratione voluptatem sequi nesciunt. Neque porro quisquam est, qui dolorem ipsum quia dolor sit amet, consectetur, adipisci velit.</p>
    <div class="toggle open"><svg width="16" height="10" viewBox="0 0 16 10"><path d="M2 8 L8 2 L14 8" fill="none" stroke="#fff" stroke-width="2"/></svg></div>
  </div>
  <div class="faq-item" style="top:347px;height:60px">
    <div class="faq-q">Sed ut perspiciatis unde omnis iste natus error sit voluptatem accusantiu?</div>
    <div class="toggle"><svg width="16" height="10" viewBox="0 0 16 10"><path d="M2 2 L8 8 L14 2" fill="none" stroke="#fff" stroke-width="2"/></svg></div>
  </div>
  <div class="faq-item" style="top:420px;height:60px">
    <div class="faq-q">Sed ut perspiciatis unde omnis iste natus error sit voluptatem accusantiu?</div>
    <div class="toggle"><svg width="16" height="10" viewBox="0 0 16 10"><path d="M2 2 L8 8 L14 2" fill="none" stroke="#fff" stroke-width="2"/></svg></div>
  </div>
  <div class="faq-item" style="top:494px;height:60px">
    <div class="faq-q">Sed ut perspiciatis unde omnis iste natus error sit voluptatem accusantiu?</div>
    <div class="toggle"><svg width="16" height="10" viewBox="0 0 16 10"><path d="M2 2 L8 8 L14 2" fill="none" stroke="#fff" stroke-width="2"/></svg></div>
  </div>
  <div class="faq-item" style="top:567px;height:60px">
    <div class="faq-q">Sed ut perspiciatis unde omnis iste natus error sit voluptatem accusantiu?</div>
    <div class="toggle"><svg width="16" height="10" viewBox="0 0 16 10"><path d="M2 2 L8 8 L14 2" fill="none" stroke="#fff" stroke-width="2"/></svg></div>
  </div>
</section>

<section class="section partners">
  <h2 class="section-title" style="top:62px">PARTNERSHIPS</h2>
  <div class="partner-card" style="left:112px">
    <div class="partner-mark"><span class="badge"></span>Meridian Saddlery</div>
    <p class="partner-copy">Meridian Saddlery is constantly designing and researching saddles and riders to find the right blend of design and craftsmanship to fit today's demands.</p>
    <div class="partner-link">READ MORE</div>
  </div>
  <div class="partner-card alt" style="left:612px">
    <div class="partner-mark"><span class="badge"></span>Ashgrove Saddlery</div>
    <p class="partner-copy">My goal is to provide the best possible fit for both horse and rider whether it is a saddle you already own, one you have on trial, or one that I carry.</p>
    <div class="partner-link">READ MORE</div>
  </div>
</section>

<section class="section contact" role="img" aria-label="Black and white close-up of a horse's eye and mane">
  <h2 class="abs serif contact-title">CONTACT US</h2>
  <div class="field" style="left:112px;top:156px;width:350px;height:46px">Name</div>
  <div class="field" style="left:112px;top:216px;width:350px;height:46px">Email *</div>
  <div class="field" style="left:112px;top:276px;width:350px;height:46px">Phone</div>
  <div class="field" style="left:473px;top:156px;width:350px;height:166px">How can we help</div>
  <div class="pill tan">SEND</div>
</section>

<footer class="section site-footer">
  <div class="footer-brand"><div class="name">LINDEN RIDGE</div><div class="sub">STABLES</div></div>
  <div class="footer-col" style="left:581px">
    <h4>QUICK LINKS</h4>
    <ul><li>Home</li><li>Services</li><li>News Room</li><li>Blog</li><li>About Us</li><li>Contact</li></ul>
  </div>
  <div class="footer-col" style="left:778px">
    <h4>CONTACT US</h4>
    <ul style="line-height:40px">
      <li style="line-height:40px"><svg width="11" height="15" viewBox="0 0 12 16"><path fill="#c3a07c" d="M6 0a6 6 0 0 0-6 6c0 4.5 6 10 6 10s6-5.5 6-10a6 6 0 0 0-6-6zm0 8.5A2.5 2.5 0 1 1 6 3.5a2.5 2.5 0 0 1 0 5z"/></svg>Cedar Falls Iowa</li>
      <li style="line-height:40px"><svg width="13" height="13" viewBox="0 0 24 24"><path fill="#c3a07c" d="M6.6 10.8a15 15 0 0 0 6.6 6.6l2.2-2.2c.3-.3.7-.4 1-.2 1.1.4 2.3.6 3.6.6.6 0 1 .4 1 1V20c0 .6-.4 1-1 1A17 17 0 0 1 3 4c0-.6.4-1 1-1h3.5c.6 0 1 .4 1 1 0 1.3.2 2.5.6 3.6.1.3 0 .7-.2 1z"/></svg>555-014-2290</li>
      <li style="line-height:40px"><svg width="15" height="11" viewBox="0 0 16 12"><rect width="16" height="12" rx="1" fill="#c3a07c"/><path d="M1 1 L8 7 L15 1" fill="none" stroke="#1c1c1c" stroke-width="1.5"/></svg>Email Us</li>
    </ul>
  </div>
  <div class="footer-rule"></div>
  <div class="copyright">Copyright © 2021, Linden Ridge Stables |. All Rights Reserved.</div>
  <div class="socials" aria-label="Social media links"><span></span><span></span><span></span></div>
</footer>

</body>
</html>
```